Brightpath EAP 2 x Flyer with Poster

Brightpath is an award-winning organisation providing dynamic and creative ways for children, young people, adults and families to make positive change and achieve fulfilling lives.
We are launching into a new area of business and starting to offer organisations Employee Assistance Program (EAP). To launch this service we need 2 flyers and a poster:
- 1 x flyer for employers
- 1 x flyer for employees
- 1 x poster (A3) for employees to be displayed around the office.
For the flyers we are after an a4 colour double sided flyer in either a A4 tri-fold to DL format or A4 bi-fold to A5 format. We are looking for a design that is simple and dynamic whilst keeping in line with our branding.
The winning designs will need to be hi-res and ready for print and also a lower res version suitable to email.
I have attached a number of files to provide further background, including:
• I have attached 3 x word doc of copy for each (2 x flyer / 1 x poster)
• Brand Guidelines
• Logo
• Our clinic flyer recently produced by a ArtHive designer for our clinic area of the business. These flyers do not have to be exactly the same as this one but should appear to be from the same organisation although a different service.
Generally we like our designs to be clear and simple.
Please don't hesitate to reach out with any Q's.

```html
<!DOCTYPE html>
<html lang="en">
<head>
<meta charset="utf-8">
<title>Brightpath EAP Flyer</title>
<link href="https://fonts.googleapis.com/css2?family=Poppins:wght@400;500;600;700&display=swap" rel="stylesheet">
<style>
:root{
  --ink:#3a3a3c;
  --sage:#6f8f76;
  --slate:#7f9da3;
  --clay:#d4aa94;
  --mist:#f2f3f5;
  --white:#ffffff;
  --photo-dark:#4a4a4a;
  --photo-light:#c9c9c9;
}
*{margin:0;padding:0;box-sizing:border-box}
html,body{width:905px;height:1200px;overflow:hidden;background:var(--white)}
body{font-family:"Poppins",sans-serif;color:var(--ink);position:relative}
.flyer{position:relative;width:905px;height:1200px;overflow:hidden}
.abs{position:absolute}

.brand{left:40px;top:26px;display:flex;align-items:center;gap:14px}
.brand-dot{width:44px;height:44px;border-radius:50%;background:var(--slate)}
.brand-name{font-size:52px;font-weight:600;color:var(--ink);letter-spacing:.5px;line-height:1}

.contact{left:26px;top:109px;width:380px;height:103px;background:var(--clay);border-radius:4px;color:var(--white);padding:14px 0 0 26px}
.contact-row{display:flex;align-items:center;gap:24px;font-size:27px;line-height:38px;font-weight:400}
.contact-row svg{width:24px;height:24px;flex:none}

.eap{left:26px;top:229px;width:380px;height:209px;background:var(--slate);border-radius:4px;color:var(--white);padding:14px 22px 0 23px}
.eap-title{display:flex;align-items:baseline;gap:12px;border-bottom:1px solid rgba(255,255,255,.55);padding-bottom:5px}
.eap-title b{font-size:31px;font-weight:600;line-height:1.1}
.eap-title span{font-size:16px;font-weight:600}
.eap p{font-size:14px;line-height:19.5px;text-align:justify;margin-top:3px}

.section-title{color:var(--sage);font-size:25px;font-weight:600;line-height:1.1}
.body-text{font-size:14.2px;line-height:19.3px;text-align:justify}

.pays{left:49px;top:470px;width:348px}
.pays .body-text{margin-top:10px}

.confidential{left:48px;top:702px;width:360px}
.confidential .lead{font-size:14px;line-height:19px;margin-top:12px;width:340px}
.conf-list{list-style:none;margin-top:12px;font-size:13px;line-height:17px}
.conf-list>li{position:relative;padding-left:26px;margin-bottom:7px}
.conf-list>li::before{content:"";position:absolute;left:3px;top:4px;width:9px;height:9px;border-radius:50%;background:var(--slate)}
.conf-or{font-weight:600;font-size:15px;padding-left:26px;margin:-2px 0 6px}
.sub-list{list-style:none;margin-top:5px}
.sub-list li{position:relative;padding-left:24px;margin-bottom:9px}
.sub-list li::before,.svc-cols li::before{content:"";position:absolute;left:2px;top:5px;width:5px;height:5px;border-top:2px solid var(--sage);border-right:2px solid var(--sage);transform:rotate(45deg)}
.conf-close{font-size:13.6px;line-height:15px;margin-top:14px;width:340px}

.services{left:424px;top:28px;width:457px;height:384px;background:var(--mist);border-radius:6px;padding:20px 0 0 20px}
.services h2{font-size:30px;font-weight:600;line-height:1.2}
.services .intro{font-size:15.5px;line-height:18.5px;margin-top:10px}
.svc-cols{display:flex;margin-top:16px;gap:18px;padding-left:7px}
.svc-cols ul{list-style:none;font-size:14px;line-height:14.5px}
.svc-cols ul:first-child{width:206px}
.svc-cols ul:last-child{width:186px}
.svc-cols li{position:relative;padding-left:18px;margin-bottom:10px}
.svc-cols li::before{top:4px}

.appt-head{left:424px;top:432px;width:457px;height:75px;background:var(--sage);border-radius:4px 4px 0 0;color:var(--white);padding:12px 0 0 20px;font-size:23px;font-weight:600;line-height:26px}
.appt-body{left:424px;top:507px;width:457px;height:207px;background:var(--mist);padding:18px 22px 0 20px}
.appt-body p{font-size:13.6px;line-height:19px;text-align:justify}
.appt-body p+p{margin-top:18px}
.link{color:var(--slate);font-weight:500}

.about{left:444px;top:730px;width:415px}
.about h2{font-size:29px;font-weight:600;line-height:1.2}
.about p{font-size:13.6px;line-height:19px;text-align:justify;margin-top:6px}

.photo{left:430px;top:927px;width:451px;height:175px;border-radius:3px;background:radial-gradient(ellipse at 50% 55%,var(--photo-light) 0%,#8a8a8a 45%,var(--photo-dark) 100%)}

.footer{left:0;top:1124px;width:905px;height:76px;background:var(--sage);color:var(--white);display:flex;align-items:center;justify-content:center;gap:12px;font-size:18px;font-weight:600}
.footer svg{width:14px;height:18px}
</style>
</head>
<body>
<main class="flyer">
  <div class="brand abs"><span class="brand-dot"></span><span class="brand-name">Brightpath</span></div>

  <div class="contact abs">
    <div class="contact-row">
      <svg viewBox="0 0 24 24" fill="#fff"><path d="M6.6 10.8a15.1 15.1 0 0 0 6.6 6.6l2.2-2.2c.3-.3.7-.4 1-.2 1.1.4 2.3.6 3.6.6.6 0 1 .4 1 1V20c0 .6-.4 1-1 1A17 17 0 0 1 3 4c0-.6.4-1 1-1h3.5c.6 0 1 .4 1 1 0 1.3.2 2.5.6 3.6.1.3 0 .7-.2 1z"/></svg>
      <span>(03) 9000 4172</span>
    </div>
    <div class="contact-row">
      <svg viewBox="0 0 24 24" fill="#fff"><path d="M2 6l10 7 10-7v12H2z"/><path d="M2 4h20l-10 7z"/></svg>
      <span>clinic@brightpath.au</span>
    </div>
  </div>

  <section class="eap abs">
    <div class="eap-title"><b>Employee</b><span>Assistance Program</span></div>
    <p>Employee Assistance Program (EAP) is a confidential employer-funded support service available to employees and immediate family members experiencing personal or work-related concerns. Immediate family include your spouse, partner, children or others living in your household.</p>
  </section>

  <section class="pays abs">
    <h2 class="section-title">Who Pays for the Service?</h2>
    <p class="body-text">Your employer will pay for an agreed number of sessions. You are not required to pay for using the Brightpath EAP service. The number of available sessions depends on the agreement we have with your employer. On your first visit we will let you know how many sessions you can access. At the end of your last available session, your counsellor can discuss options for further counselling or support if needed.</p>
  </section>

  <section class="confidential abs">
    <h2 class="section-title">Is it Confidential?</h2>
    <p class="lead">All employee personal information collated by Brightpath during the provision of counselling services will remain confidential and secure except when:</p>
    <ul class="conf-list">
      <li>It is subpoenaed by a court, or</li>
      <li>Failure to disclose the information would place the employee and/or another person at risk;</li>
    </ul>
    <p class="conf-or">or</p>
    <ul class="conf-list">
      <li>The employee’s prior consent has been obtained to:
        <ul class="sub-list">
          <li>provide a written report to another professional or agency eg. The Employer, GP or lawyer; or</li>
          <li>discuss the material with another person eg. The Employer or GP.</li>
        </ul>
      </li>
    </ul>
    <p class="conf-close">Confidentiality and limitations of confidentiality are explained to employees at the beginning of the counselling process.</p>
  </section>

  <section class="services abs">
    <h2>Counselling Services</h2>
    <p class="intro">EAP is provided for a variety of personal,<br>emotional and work-related matters including:</p>
    <div class="svc-cols">
      <ul>
        <li>Anxiety</li>
        <li>Depression &amp; emotional<br>wellbeing</li>
        <li>Workplace conflict or<br>disharmony</li>
        <li>Coping with<br>organisational change</li>
        <li>Stress and burnout<br>Bullying</li>
        <li>Sexual harassment</li>
        <li>Self-esteem</li>
      </ul>
      <ul>
        <li>Reactions to traumatic<br>or distressing events</li>
        <li>Critical incidents</li>
        <li>Grief &amp; bereavement</li>
        <li>Substance misuse</li>
        <li>Domestic violence</li>
        <li>Interpersonal<br>relationships</li>
        <li>Schooling and study<br>difficulties.</li>
      </ul>
    </div>
  </section>

  <h2 class="appt-head abs">How do I make an EAP<br>Appointment?</h2>
  <section class="appt-body abs">
    <p>The Brightpath intake team are trained in handling distressing incidents and will assist in making your initial appointment. We will respond to your call and book your initial appointment within the next working day, or at a time convenient to you.</p>
    <p>You can make a confidential appointment directly with Brightpath through our direct line on <span class="link">03 9000 4172</span> or via <span class="link">clinic@brightpath.au</span></p>
  </section>

  <section class="about abs">
    <h2>About Brightpath</h2>
    <p>Brightpath provides a confidential and effective counselling process that is solution-focused and practical. The service is aimed at enhancing wellbeing and mental health, and can be accessed via face-to-face consultations, and by Telehealth or phone. Accessing assistance is an act of independence and strength which can empower you to make positive changes in your life.</p>
  </section>

  <div class="photo abs" role="img" aria-label="Black and white photo of many hands joined with fingertips touching in a circle"></div>

  <footer class="footer abs">
    <svg viewBox="0 0 14 18" fill="#fff"><path d="M7 0a7 7 0 0 0-7 7c0 5 7 11 7 11s7-6 7-11a7 7 0 0 0-7-7zm0 9.5A2.5 2.5 0 1 1 7 4.5a2.5 2.5 0 0 1 0 5z"/></svg>
    <span>Harbourview Building&nbsp; 42 Linden Ave, Northvale VIC 3999</span>
  </footer>
</main>
</body>
</html>
```